Brintell's Business Card

I need some designs for a new business card including the new logo attached. An old example of our business card is also attached to show all the data that should be included on the new design.
**I added some more examples someone had mocked up**

Contact Information for Business Card

Should include all info on other examples uploaded.

```html
<!DOCTYPE html>
<html lang="en">
<head>
<meta charset="UTF-8">
<title>Brintell's Business Card</title>
<link href="https://fonts.googleapis.com/css2?family=Montserrat:wght@500;600;700;800&display=swap" rel="stylesheet">
<style>
  :root {
    --page-bg: #e9e9ea;
    --card-dark: #2f2f30;
    --card-darker: #262627;
    --brand-blue: #0a6fc0;
    --brand-red: #e3222b;
    --white: #ffffff;
    --muted: #d9d9d9;
  }
  * { box-sizing: border-box; margin: 0; padding: 0; }
  html, body {
    width: 1200px; height: 802px; overflow: hidden;
    background: var(--page-bg);
    font-family: "Montserrat", sans-serif;
  }
  .stage {
    width: 1200px; height: 802px;
    display: flex; align-items: center; justify-content: center; gap: 40px;
  }
  .card {
    position: relative;
    width: 540px; height: 309px;
    background: var(--card-dark);
    overflow: hidden;
    box-shadow: 0 10px 28px rgba(0,0,0,0.25);
  }
  /* Front */
  .card-front .corner {
    position: absolute; top: 0; right: 0;
    width: 260px; height: 200px;
  }
  .card-front .mark-circle {
    position: absolute; top: 34px; right: 44px;
    width: 170px; height: 170px; border-radius: 50%;
    background: var(--white);
  }
  .front-text {
    position: absolute; left: 34px; top: 40px;
    color: var(--white);
  }
  .front-text .brand-name {
    font-size: 46px; font-weight: 700; letter-spacing: 1px; line-height: 1;
  }
  .front-text .person-name {
    margin-top: 34px;
    font-size: 21px; font-weight: 700; letter-spacing: 0.5px;
  }
  .contact-list { list-style: none; margin-top: 18px; }
  .contact-list li {
    display: flex; align-items: center; gap: 8px;
    font-size: 13px; font-weight: 500; line-height: 1.55;
  }
  .contact-list svg { width: 12px; height: 12px; fill: var(--white); }
  .credentials {
    margin-top: 16px;
    font-size: 13px; font-weight: 600; letter-spacing: 0.4px; line-height: 1.45;
  }
  /* Back */
  .card-back { background: var(--card-darker); }
  .pattern-field {
    position: absolute; inset: 0;
    background: radial-gradient(ellipse at 70% 40%, #343435 0%, #262627 70%);
  }
  .back-content {
    position: absolute; inset: 0;
    display: flex; flex-direction: column; align-items: center; justify-content: center;
  }
  .back-logo {
    display: flex; align-items: center; gap: 10px;
  }
  .back-logo .dot {
    width: 34px; height: 34px; border-radius: 50%;
    background: var(--brand-blue);
  }
  .back-logo .brand-name {
    font-size: 34px; font-weight: 700; color: var(--brand-blue); letter-spacing: 1px;
  }
  .service-area {
    margin-top: 14px;
    background: var(--brand-red); color: var(--white);
    font-size: 15px; font-weight: 500;
    padding: 4px 12px;
  }
  .call-line {
    margin-top: 14px;
    color: var(--white);
    font-size: 11px; font-weight: 700; letter-spacing: 0.4px;
  }
</style>
</head>
<body>
<main class="stage">
  <section class="card card-front">
    <svg class="corner" viewBox="0 0 260 200" aria-hidden="true">
      <polygon points="60,0 260,0 260,200" fill="var(--brand-blue)"/>
    </svg>
    <div class="mark-circle"></div>
    <div class="front-text">
      <h1 class="brand-name">BRINTELL'S</h1>
      <p class="person-name">DALE MERCER</p>
      <ul class="contact-list">
        <li>
          <svg viewBox="0 0 24 24"><path d="M6.6 10.8a15.1 15.1 0 0 0 6.6 6.6l2.2-2.2c.3-.3.7-.4 1-.2 1.1.4 2.3.6 3.6.6.6 0 1 .4 1 1V20c0 .6-.4 1-1 1C10.6 21 3 13.4 3 4c0-.6.4-1 1-1h3.5c.6 0 1 .4 1 1 0 1.3.2 2.5.6 3.6.1.3 0 .7-.2 1z"/></svg>
          555.014.2290
        </li>
        <li>
          <svg viewBox="0 0 24 24"><path d="M2 5h20v14H2z M4 7v.5l8 5 8-5V7l-8 5z" fill-rule="evenodd"/></svg>
          hvacbrintell@mailbox.com
        </li>
      </ul>
      <p class="credentials">LICENSED &amp; INSURED<br>FAMILY OWNED &amp; OPERATED</p>
    </div>
  </section>

  <section class="card card-back">
    <div class="pattern-field" role="img" aria-label="Repeating embossed brand symbol pattern across the card"></div>
    <div class="back-content">
      <div class="back-logo">
        <span class="dot"></span>
        <span class="brand-name">BRINTELL'S</span>
      </div>
      <p class="service-area">Serves Maple Hollow, IA &amp; Surrounding Areas</p>
      <p class="call-line">CALL TODAY FOR ALL YOUR HVAC, REFRIGERATION &amp; PLUMBING NEEDS</p>
    </div>
  </section>
</main>
</body>
</html>
```